Design the 1st of 6 postcards marketing government software

We sell permit software to government agencies and need an eye catching postcard for our direct mailing campaign. This will be the first card in a series of 6. Designs should use our company color palette found in the attached "logo master details.pdf" and resemble our website design at tarvendo.com. The postcard should have a modern and minimalistic feel and should use imagery of "small town main street" such as the attached "retail-store" photo. The front of the card should display the headline "Automate Your Plan Review Workflow and Cut Review Times In Half" and feature our logo. The back of the card should prominently display our website "Tarvendo.com" and also feature our 4 products as seen in the solutions section of our home page (Citizen Access, Plan Review, Permits, Inspections). You can use the same 4 icons but don't include the lengthy descriptions. two .indd files have been included as a template for the size of the card and blank space required on the back. Also include our phone number 1 (833) 517-2940 x5 and email sales@tarvendo.com on the back of the card, you can optionally use our pin icon as a watermark in the background, it can be oversized and run of the page if you want, similar to the trusted clients section of our home page.

```html
<!DOCTYPE html>
<html lang="en">
<head>
<meta charset="utf-8">
<title>Tarvendo Postcard 1 – Front and Back</title>
<link href="https://fonts.googleapis.com/css2?family=Montserrat:wght@400;500;600;700&display=swap" rel="stylesheet">
<style>
  :root{
    --page:#ffffff;
    --ink:#000000;
    --white:#ffffff;
    --brand-blue:#2a7fd0;
    --navy:#111b38;
    --logo-dark:#1a1a1a;
    --street-sky:#4f95d6;
    --street-warm:#b9865a;
    --street-shadow:#1d2a3a;
    --device-tone:#2b3a5c;
    --divider:#5c6787;
  }
  *{margin:0;padding:0;box-sizing:border-box}
  html,body{width:1200px;height:1179px;overflow:hidden;background:var(--page)}
  body{position:relative;font-family:"Montserrat",sans-serif}

  .card{position:absolute}

  /* back card */
  .card-back{left:466px;top:539px;width:692px;height:597px;background:var(--white)}
  .back-logo{position:absolute;left:0;right:0;top:18px;text-align:center;font-weight:600;font-size:18px;color:var(--logo-dark);letter-spacing:.5px}
  .device-visual{position:absolute;left:142px;top:59px;width:427px;height:240px;border-radius:8px;
    background:linear-gradient(135deg,var(--device-tone),#1a2542 60%,#c9ced8)}
  .solutions{position:absolute;left:0;top:311px;width:692px;height:214px;background:var(--navy);color:var(--white)}
  .solutions-title{position:absolute;left:0;right:0;top:22px;text-align:center;font-weight:600;font-size:19px;letter-spacing:.3px;white-space:nowrap}
  .solution{position:absolute;top:102px;width:160px;margin-left:-80px;text-align:center}
  .solution svg{display:block;margin:0 auto 8px;width:26px;height:26px}
  .solution-name{font-size:14px;font-weight:400;white-space:nowrap}
  .divider{position:absolute;top:110px;width:1px;height:36px;background:var(--divider)}
  .contact-bar{position:absolute;left:0;top:525px;width:692px;height:72px;background:var(--ink);color:var(--white);
    display:flex;align-items:center;justify-content:center;gap:30px;font-weight:600;font-size:14px;white-space:nowrap}
  .contact-item{display:flex;align-items:center;gap:6px}
  .contact-item svg{width:15px;height:15px}

  /* front card */
  .card-front{left:31px;top:28px;width:652px;height:561px;background:var(--ink)}
  .front-top{position:absolute;left:0;top:0;width:652px;height:254px;background:var(--white)}
  .street-photo{position:absolute;left:17px;top:20px;width:618px;height:361px;border-radius:20px;
    background:linear-gradient(180deg,var(--street-sky) 0%,#8fbbe0 30%,var(--street-warm) 55%,var(--street-shadow) 85%)}
  .logo-tab{position:absolute;left:0;top:151px;width:231px;height:103px;background:var(--white);
    border-radius:0 20px 20px 0;display:flex;align-items:center;padding-left:35px}
  .logo-tab span{font-weight:600;font-size:34px;color:var(--logo-dark)}
  .headline{position:absolute;left:50px;top:412px;line-height:38px;white-space:nowrap}
  .headline-lead{display:block;color:var(--white);font-weight:400;font-size:37px;letter-spacing:-.5px}
  .headline-main{display:block;color:var(--brand-blue);font-weight:700;font-size:31px;letter-spacing:-1px}
</style>
</head>
<body>

<section class="card card-back" aria-label="Postcard back">
  <div class="back-logo">Tarvendo</div>
  <div class="device-visual" role="img" aria-label="Laptop and phone showing the Tarvendo website home page"></div>

  <div class="solutions">
    <h2 class="solutions-title">Innovative Solutions Designed For You</h2>

    <div class="solution" style="left:104px">
      <svg viewBox="0 0 26 26" fill="none" stroke="#fff" stroke-width="1.3"><rect x="5" y="3" width="16" height="12" rx="1"/><path d="M2 19h22l-2 4H4z"/><path d="M9 9h8M9 12h5"/></svg>
      <div class="solution-name">Citizen Acess</div>
    </div>
    <div class="divider" style="left:187px"></div>

    <div class="solution" style="left:265px">
      <svg viewBox="0 0 26 26" fill="none" stroke="#fff" stroke-width="1.3"><rect x="3" y="4" width="20" height="15"/><path d="M13 2v2M7 19l-2 5M19 19l2 5M7 15l4-5 3 3 5-6"/></svg>
      <div class="solution-name">Plan Review</div>
    </div>
    <div class="divider" style="left:356px"></div>

    <div class="solution" style="left:435px">
      <svg viewBox="0 0 26 26" fill="none" stroke="#fff" stroke-width="1.3"><rect x="4" y="2" width="14" height="20"/><path d="M7 6h8M7 9h8M7 12h8M7 15h5"/><rect x="15" y="14" width="7" height="10"/></svg>
      <div class="solution-name">Permit</div>
    </div>
    <div class="divider" style="left:503px"></div>

    <div class="solution" style="left:584px">
      <svg viewBox="0 0 26 26" fill="none" stroke="#fff" stroke-width="1.3"><rect x="4" y="3" width="15" height="20"/><path d="M9 2h5v3H9z"/><circle cx="14" cy="14" r="4"/><path d="M17 17l5 5"/></svg>
      <div class="solution-name">Inspection</div>
    </div>
  </div>

  <div class="contact-bar">
    <div class="contact-item">
      <svg viewBox="0 0 16 16" fill="#fff"><path d="M3.5 1l2.5 3-1.5 2c1 2 3 4 5 5l2-1.5 3 2.5-1.5 2.5C7 15 1 9 1 2.5z"/></svg>
      <span>1 (833) 517-2940</span>
    </div>
    <div class="contact-item">
      <svg viewBox="0 0 16 16" fill="none" stroke="#fff" stroke-width="1.5"><circle cx="8" cy="8" r="3"/><path d="M11 8v1.5a2 2 0 0 0 4 0V8a7 7 0 1 0-3 5.7"/></svg>
      <span>sales@tarvendo.com</span>
    </div>
    <div class="contact-item">
      <svg viewBox="0 0 16 16" fill="none" stroke="#fff" stroke-width="1.2"><circle cx="8" cy="8" r="7"/><ellipse cx="8" cy="8" rx="3" ry="7"/><path d="M1 8h14M2.5 4.5h11M2.5 11.5h11"/></svg>
      <span>www.tarvendo.com</span>
    </div>
  </div>
</section>

<section class="card card-front" aria-label="Postcard front">
  <div class="front-top"></div>
  <div class="street-photo" role="img" aria-label="Sunlit small town main street with brick buildings, crosswalk and blue sky"></div>
  <div class="logo-tab"><span>Tarvendo</span></div>
  <h1 class="headline">
    <span class="headline-lead">Automate</span>
    <span class="headline-main">Your Plan Review Workflow and</span>
    <span class="headline-main">Cut Review Times In Half</span>
  </h1>
</section>

</body>
</html>
```